Online Greeting Card Marketplace redesign

PennedNotes.com is a two-sided greeting card marketplace. Buyers purchase hand-made cards online, indicating their message. Sellers hand-write the message and mail directly to recipient.

We are getting decent foot traffic but low sales. I'm also not drawing a lot of Card Designers to sell their products. Feedback has been that it's cluttered, boring, and out of date.

I've always enjoyed vibes such as Lana Brookfield and Delia Hartwell. I was going for pale blues and chocolate browns (as can be seen in PennedNotes Friendbook and Chirpline pages).

Attached document is my not-so-great attempt to redesign, which is uninviting and unpolished.

Need a new homepage and a second similar page when shopping (click on any category to see what I mean, e.g. Halloween).
Updates

Industry/Entity Type

Shopping

Requirements
Must have
• I think my logo (stick drawing of a man with an envelope) is what is currently driving a lot of traffic and should stay in the design, pending minor tweaks.

I'll need all the details of the final design to give to the programmers (font styles, color numbers, etc).

Nice to have
• I was thinking of a dotted frame to surround each picture? White Pearl luminescent or a metallic? I just don't know if it works.

```html
<!DOCTYPE html>
<html lang="en">
<head>
<meta charset="utf-8">
<title>PennedNotes.com — Halloween</title>
<link href="https://fonts.googleapis.com/css2?family=Lato:wght@400;700&family=Pacifico&display=swap" rel="stylesheet">
<style>
:root{
  --teal:#5bb8c9;
  --teal-dark:#3f9fb2;
  --sky:#d6f0f6;
  --sky-stripe:#c9e9f1;
  --page:#f7f7f7;
  --ink:#3a2a22;
  --text:#555;
  --muted:#8a8a8a;
  --red:#e8585a;
  --indigo:#5b6cae;
  --orange:#f08c1a;
  --yellow:#f6e34a;
  --pink:#ef4a6c;
  --white:#fff;
}
*{box-sizing:border-box;margin:0;padding:0}
html,body{width:1155px;height:1200px;overflow:hidden}
body{position:relative;background:var(--page);font-family:'Lato',sans-serif;color:var(--text)}
.topbar{position:absolute;left:0;top:0;width:1155px;height:44px;background:var(--teal)}
.topbar::after{content:"";position:absolute;left:0;top:44px;width:100%;height:10px;
  background:radial-gradient(circle at 9px 0,var(--teal) 8px,transparent 8.5px) 0 0/18px 10px repeat-x}
.masthead{position:absolute;left:0;top:44px;width:1155px;height:120px;
  background:repeating-linear-gradient(90deg,var(--sky) 0 4px,var(--sky-stripe) 4px 6px)}
.welcome{position:absolute;left:152px;top:16px;font-size:11.5px;color:var(--white)}
.welcome a{color:var(--yellow);text-decoration:none}
.search{position:absolute;left:529px;top:12px;width:302px;height:23px;background:#eefafc;border:1px solid #bfe3ea;border-radius:3px;font-size:10px;color:#7a9aa2;padding:5px 9px;letter-spacing:.3px}
.search svg{position:absolute;right:6px;top:4px}
.cart-icon{position:absolute;left:920px;top:10px}
.cart-label{position:absolute;left:964px;top:6px;font-size:9.5px;font-weight:700;color:var(--white)}
.cart-count{position:absolute;left:962px;top:20px;width:33px;height:15px;background:var(--pink);border-radius:2px;color:var(--white);font-size:10px;font-weight:700;text-align:center;line-height:15px}
.logo{position:absolute;left:142px;top:70px;display:flex;align-items:center;gap:10px}
.logo-dot{width:30px;height:30px;border-radius:50%;background:var(--teal)}
.logo-name{font-size:30px;font-weight:700;color:var(--ink);letter-spacing:-.5px}
.nav{position:absolute;top:104px;left:559px;display:flex;gap:20px;font-size:11.5px;font-weight:700;text-transform:uppercase;letter-spacing:-.1px}
.nav a{text-decoration:none;padding:4px 7px;line-height:14px}
.nav .holidays{color:var(--red);border:1px dotted #777;background:#f4fbfd}
.nav .everyday{color:var(--teal)}
.nav .birthdays{color:var(--indigo)}
.nav .all{color:var(--orange)}
.crumb{position:absolute;left:149px;top:179px;font-size:13px;color:#444}
.title{position:absolute;left:147px;top:202px;font-family:'Pacifico',cursive;font-size:40px;color:var(--ink);font-weight:400}
.toolbar{position:absolute;left:149px;width:856px;height:26px;display:flex;align-items:center;font-size:11.5px;color:#555}
.toolbar.top{top:277px}
.toolbar.bottom{top:1050px}
.select{display:inline-flex;align-items:center;height:24px;border:1px solid #444;border-radius:3px;background:var(--white);font-size:11.5px;padding-left:8px;margin-left:14px;overflow:hidden}
.select .arrows{width:22px;height:100%;margin-left:4px;background:#cfe8ee;display:flex;flex-direction:column;align-items:center;justify-content:center;gap:2px}
.select .arrows i{width:0;height:0;border-left:4px solid transparent;border-right:4px solid transparent}
.select .arrows i.up{border-bottom:5px solid #8fb4bd}
.select .arrows i.down{border-top:5px solid #8fb4bd}
.perpage{margin-left:32px}
.pager{margin-left:auto;display:flex;align-items:center;gap:9px;font-size:11.5px;color:#444}
.pager .current{font-weight:700;color:#111}
.next{margin-left:16px;width:58px;height:26px;background:var(--teal);border-bottom:2px solid var(--teal-dark);border-radius:2px;color:var(--white);font-weight:700;font-size:13px;text-align:center;line-height:24px}
.grid{position:absolute;left:151px;top:331px;display:grid;grid-template-columns:repeat(4,204px);column-gap:12px;row-gap:36px}
.card{width:204px}
.frame{border:1.5px dotted #333;padding:7px;height:209px;background:var(--white)}
.art{width:100%;height:100%}
.card h2{margin-top:14px;font-size:17px;font-weight:700;color:#3a3a3a}
.card .meta{font-size:11.5px;color:var(--muted);line-height:15px;margin-top:2px}
.price{display:inline-block;margin-top:14px;padding:0 12px;height:24px;line-height:24px;background:var(--teal);border-bottom:2px solid var(--teal-dark);color:var(--white);font-weight:700;font-size:13px;border-radius:1px}
.footer{position:absolute;left:0;top:1136px;width:1155px;height:64px;background:var(--teal)}
.footer::before{content:"";position:absolute;left:0;top:-8px;width:100%;height:8px;
  background:radial-gradient(circle at 9px 9px,var(--teal) 8px,transparent 8.5px) 0 0/18px 9px repeat-x}
.copyright{position:absolute;left:152px;top:24px;font-size:10px;color:var(--white)}
.footer-links{position:absolute;right:149px;top:22px;display:flex;gap:22px;font-size:10px;color:var(--white);align-items:center}
.footer-links .social{font-weight:700;font-size:11px}
</style>
</head>
<body>
<header>
  <div class="topbar">
    <p class="welcome">Welcome Visitor you can <a href="#">Sign In</a> or <a href="#">create an account</a></p>
    <div class="search">SEARCH
      <svg width="14" height="14" viewBox="0 0 14 14"><circle cx="8" cy="6" r="4.5" fill="none" stroke="#7a9aa2" stroke-width="1.5"/><line x1="4.8" y1="9.2" x2="1.5" y2="12.5" stroke="#7a9aa2" stroke-width="1.8"/></svg>
    </div>
    <svg class="cart-icon" width="28" height="24" viewBox="0 0 28 24"><path d="M8 9 L12 2 M20 9 L16 2" stroke="#fff" stroke-width="2.2" fill="none"/><path d="M2 9 H26 L23 22 H5 Z" fill="none" stroke="#fff" stroke-width="2.6" stroke-linejoin="round"/><line x1="5" y1="14" x2="23" y2="14" stroke="#fff" stroke-width="2"/></svg>
    <span class="cart-label">CART</span>
    <span class="cart-count">2</span>
  </div>
  <div class="masthead"></div>
  <div class="logo"><span class="logo-dot"></span><span class="logo-name">pennednotes.com</span></div>
  <nav class="nav">
    <a class="holidays" href="#">Upcoming Holidays</a>
    <a class="everyday" href="#">Every Day Cards</a>
    <a class="birthdays" href="#">Birthdays</a>
    <a class="all" href="#">All Categories</a>
  </nav>
</header>

<main>
  <p class="crumb">Home /</p>
  <h1 class="title">Halloween</h1>

  <div class="toolbar top">
    Sort by <span class="select">Card Number<span class="arrows"><i class="up"></i><i class="down"></i></span></span>
    <span class="perpage">Per Page</span> <span class="select">10<span class="arrows"><i class="up"></i><i class="down"></i></span></span>
    <div class="pager"><span class="current">1</span><span>2</span><span>3</span><span>4</span><span>5</span><span>6</span><span>...</span><span>15</span><span class="next">Next</span></div>
  </div>

  <section class="grid">
    <article class="card"><div class="frame"><div class="art" role="img" aria-label="Papercut card: bats flying across a full moon" style="background:radial-gradient(circle at 45% 45%,#e8e8e8 0 42%,#2a2a2a 43%)"></div></div>
      <h2>Halloween</h2><p class="meta">By Creator<br>Card Number: SKU17597</p><span class="price">$7.00</span></article>
    <article class="card"><div class="frame"><div class="art" role="img" aria-label="Papercut card: white wolf howling at a crescent moon" style="background:linear-gradient(160deg,#111 0 55%,#cfcfcf 56%,#111 80%)"></div></div>
      <h2>Halloween</h2><p class="meta">By Creator<br>Card Number: SKU17734</p><span class="price">$7.00</span></article>
    <article class="card"><div class="frame"><div class="art" role="img" aria-label="Papercut card: sailing ship on dark waves" style="background:linear-gradient(170deg,#dfe8ee,#f4f4f4 45%,#1e2a44 80%)"></div></div>
      <h2>Labor Day</h2><p class="meta">By Creator<br>Card Number: SKU17738</p><span class="price">$7.00</span></article>
    <article class="card"><div class="frame"><div class="art" role="img" aria-label="Papercut card: black horse silhouette in a frame" style="background:linear-gradient(135deg,#e6e6e6,#5a5a5a 55%,#1a1a1a)"></div></div>
      <h2>Labor Day</h2><p class="meta">By Creator<br>Card Number: SKU17740</p><span class="price">$7.00</span></article>

    <article class="card"><div class="frame"><div class="art" role="img" aria-label="Watercolour card: purple whale with a diver underwater" style="background:radial-gradient(ellipse at 55% 50%,#a592a8 0 30%,#f6f4f6 60%)"></div></div>
      <h2>Halloween</h2><p class="meta">By Creator<br>Card Number: SKU17597</p><span class="price">$7.00</span></article>
    <article class="card"><div class="frame"><div class="art" role="img" aria-label="Chalkboard card: beehive with a You Are So Sweet message" style="background:radial-gradient(circle at 50% 50%,#4a4a4a,#262626)"></div></div>
      <h2>Halloween</h2><p class="meta">By Creator<br>Card Number: SKU17734</p><span class="price">$7.00</span></article>
    <article class="card"><div class="frame"><div class="art" role="img" aria-label="Quilled paper card: colourful spiral flowers on stems" style="background:linear-gradient(180deg,#eef4f7,#e3eef2)"></div></div>
      <h2>Labor Day</h2><p class="meta">By Creator<br>Card Number: SKU17738</p><span class="price">$7.00</span></article>
    <article class="card"><div class="frame"><div class="art" role="img" aria-label="Painted card: bluebird perched on a flowering branch" style="background:radial-gradient(circle at 55% 45%,#9ab0cf 0 18%,#f6eaa8 45%)"></div></div>
      <h2>Labor Day</h2><p class="meta">By Creator<br>Card Number: SKU17740</p><span class="price">$7.00</span></article>
  </section>

  <div class="toolbar bottom">
    Sort by <span class="select">Card Number<span class="arrows"><i class="up"></i><i class="down"></i></span></span>
    <span class="perpage">Per Page</span> <span class="select">10<span class="arrows"><i class="up"></i><i class="down"></i></span></span>
    <div class="pager"><span class="current">1</span><span>2</span><span>3</span><span>4</span><span>5</span><span>6</span><span>...</span><span>15</span><span class="next">Next</span></div>
  </div>
</main>

<footer class="footer">
  <p class="copyright">All rights reserved © 2011-2013 Penned Notes</p>
  <div class="footer-links"><span>About Us/FAQ</span><span>Contact</span><span>Follow Us</span><span class="social">Chirpline</span><span class="social">Friendbook</span></div>
</footer>
</body>
</html>
```